Security camera surveillance warning Sign

Security Camera Sign 11" x 11" Red, Yellow and Black (White Background)
I would like a line drawing of camera image attached.
Wording: All Suspicious or Criminal Activity Will Be Reported!
WARNING
24 HOUR SURVEILLANCE

Industry/Entity Type

Security

Colors
ec1f27
000000
ffc214

Requirements
Nice to have
• I uploaded a sign and would like the new design look something like that

```html
<!DOCTYPE html>
<html lang="en">
<head>
<meta charset="UTF-8">
<title>24 Hour Surveillance Warning Sign</title>
<link rel="stylesheet" href="https://fonts.googleapis.com/css2?family=Roboto+Slab:wght@800&family=Archivo+Black&family=Orbitron:wght@700&family=Roboto+Condensed:wght@700&display=swap">
<style>
  :root {
    --sign-red: #ec1f27;
    --sign-yellow: #ffc214;
    --sign-yellow-bright: #fff200;
    --sign-black: #000000;
    --sign-white: #ffffff;
    --camera-light: #d9d9d9;
    --camera-mid: #8a8a8a;
    --camera-dark: #2a2a2a;
  }
  html, body {
    margin: 0;
    padding: 0;
    width: 1200px;
    height: 1200px;
    overflow: hidden;
    background: var(--sign-white);
  }
  .sign {
    position: relative;
    width: 1200px;
    height: 1200px;
    background: var(--sign-white);
    overflow: hidden;
  }
  .header-band {
    position: absolute;
    left: 0;
    top: 16px;
    width: 1200px;
    height: 224px;
  }
  .camera-illustration {
    position: absolute;
    left: 0;
    top: 0;
    width: 1200px;
    height: 1200px;
    pointer-events: none;
  }
  .hours-badge,
  .label-box {
    position: absolute;
    left: 54px;
  }
  .hours-badge { top: 466px; width: 242px; height: 148px; }
  .label-hour { top: 710px; width: 366px; height: 116px; }
  .label-surveillance { top: 872px; width: 966px; height: 118px; }
  .notice-band {
    position: absolute;
    left: 6px;
    top: 1040px;
    width: 1188px;
    height: 120px;
  }
  .headline-text {
    font-family: "Roboto Slab", Georgia, serif;
    font-weight: 800;
    fill: var(--sign-red);
  }
  .hours-text {
    font-family: "Archivo Black", Arial, sans-serif;
    fill: var(--sign-white);
  }
  .label-text {
    font-family: "Orbitron", Arial, sans-serif;
    font-weight: 700;
    fill: var(--sign-yellow-bright);
    stroke: var(--sign-yellow);
    stroke-width: 1.5px;
  }
  .notice-text {
    font-family: "Roboto Condensed", Arial, sans-serif;
    font-weight: 700;
    fill: var(--sign-white);
  }
</style>
</head>
<body>
<main class="sign">

  <svg class="header-band" viewBox="0 0 1200 224" aria-label="Warning">
    <rect class="header-rule" x="0" y="0" width="1200" height="16" fill="var(--sign-black)"/>
    <rect class="header-fill" x="0" y="16" width="1200" height="188" fill="var(--sign-yellow-bright)"/>
    <rect class="header-rule" x="0" y="204" width="1200" height="20" fill="var(--sign-black)"/>
    <text class="headline-text" x="190" y="170" font-size="164" textLength="834" lengthAdjust="spacingAndGlyphs">WARNING</text>
  </svg>

  <svg class="camera-illustration" viewBox="0 0 1200 1200" role="img" aria-label="Line drawing of a wall-mounted security camera in housing on a bracket">
    <defs>
      <linearGradient id="camera-tone" x1="0" y1="0" x2="1" y2="1">
        <stop offset="0" stop-color="var(--camera-light)"/>
        <stop offset="0.55" stop-color="var(--camera-mid)"/>
        <stop offset="1" stop-color="var(--camera-dark)"/>
      </linearGradient>
    </defs>
    <path fill="url(#camera-tone)" d="M350 280 H1040 Q1070 280 1070 310 V540 H1080 Q1110 540 1110 570 V800 Q1110 830 1080 830 H730 Q700 830 700 800 V660 H350 Q320 660 320 630 V310 Q320 280 350 280 Z"/>
  </svg>

  <svg class="hours-badge" viewBox="0 0 242 148" aria-label="24">
    <rect x="0" y="0" width="242" height="148" fill="var(--sign-red)"/>
    <text class="hours-text" x="121" y="122" font-size="136" text-anchor="middle" textLength="190" lengthAdjust="spacingAndGlyphs">24</text>
  </svg>

  <svg class="label-box label-hour" viewBox="0 0 366 116" aria-label="Hour">
    <rect x="0" y="0" width="366" height="116" fill="var(--sign-black)"/>
    <text class="label-text" x="36" y="90" font-size="86" textLength="310" lengthAdjust="spacingAndGlyphs">HOUR</text>
  </svg>

  <svg class="label-box label-surveillance" viewBox="0 0 966 118" aria-label="Surveillance">
    <rect x="0" y="0" width="966" height="118" fill="var(--sign-black)"/>
    <text class="label-text" x="36" y="92" font-size="88" textLength="904" lengthAdjust="spacingAndGlyphs">SURVEILLANCE</text>
  </svg>

  <svg class="notice-band" viewBox="0 0 1188 120" aria-label="All Suspicious or Criminal Activity Will Be Recorded">
    <rect x="0" y="0" width="1188" height="120" rx="54" ry="54" fill="var(--sign-red)"/>
    <text class="notice-text" x="594" y="74" font-size="42" text-anchor="middle" textLength="1124" lengthAdjust="spacingAndGlyphs">All Suspicious or Criminal Activity Will Be Recorded</text>
  </svg>

</main>
</body>
</html>
```